Skatepark, and Teenage Music/Recreation Venue needs logo, business card and letterhead. Website desi

- Logo, Letterhead & Business Card design for a new start Skatepark and Youth Venue called "The Orbit" (Pty.Ltd company) in Australia.

- Website and App design will follow within 6-months.

- Facility centered around world class skatepark which incorporates the use of innovative technology applications to enhance consumer experience, it will also provide a live entertainment & music venue for teenagers.

- Appearance should appeal to the 'mature' teenage population, the aim is provide an excellent membership experience which can be associated with the club brand.

Overall the design should communicate:
Excitement, energy, exclusivity and style

- Clean and modern fonts and styling preferred.
- Logos the I personally like: Brinmore, Quellstone, (but they don't have to be round!)
- Generally I prefer understated business cards that are subtlety/elegently distinct
- ideally the logo would be expected to standalone if no text were available. (if that makes sense?)

Business

The Orbit

```html
<!DOCTYPE html>
<html lang="en">
<head>
<meta charset="utf-8">
<title>The Orbit — Stationery Set</title>
<link rel="stylesheet" href="https://fonts.googleapis.com/css2?family=Arimo:wght@400;700&display=swap">
<style>
  :root {
    --ink: #1f1f1f;
    --accent-orange: #c8701e;
    --mark-red: #d4281c;
    --frame-grey: #c9c9c9;
    --card-border: #1a1a1a;
    --sheet-border: #dcdcdc;
    --paper: #ffffff;
    --faint: #f4eeee;
    --faint-text: #ead9d7;
  }
  * { box-sizing: border-box; margin: 0; padding: 0; }
  html, body { width: 1200px; height: 800px; overflow: hidden; background: var(--paper); }
  body { position: relative; font-family: "Arimo", Arial, sans-serif; color: var(--ink); }

  .canvas-frame {
    position: absolute; left: 1px; top: 1px; width: 1198px; height: 798px;
    border: 1px solid var(--frame-grey);
  }

  .brand {
    position: absolute; display: flex; align-items: center; gap: 8px;
    transform: translate(-50%, -50%);
    font-family: "Arimo", Arial, sans-serif; font-weight: 400;
    color: var(--ink); letter-spacing: 0.04em; white-space: nowrap;
  }
  .brand-dot { border-radius: 50%; background: var(--mark-red); flex: none; }

  .brand--hero { left: 310px; top: 190px; font-size: 40px; }
  .brand--hero .brand-dot { width: 22px; height: 22px; }

  .card {
    position: absolute; left: 117px; width: 451px; height: 212px;
    border: 2px solid var(--card-border); background: var(--paper);
  }
  .card--front { top: 336px; }
  .card--back { top: 563px; }

  .card--front .brand { left: 225px; top: 60px; font-size: 20px; gap: 5px; }
  .card--front .brand-dot { width: 11px; height: 11px; }
  .card--back .brand { left: 225px; top: 110px; font-size: 34px; }
  .card--back .brand-dot { width: 18px; height: 18px; }

  .card-holder {
    position: absolute; left: 40px; top: 143px;
    color: var(--accent-orange); font-size: 16px; line-height: 19px;
  }
  .card-divider {
    position: absolute; left: 211px; top: 105px; width: 2px; height: 76px;
    background: var(--accent-orange);
  }
  .card-contact {
    position: absolute; left: 225px; top: 106px;
    font-size: 14.5px; line-height: 20.5px; color: var(--ink);
  }
  .label { color: var(--accent-orange); }

  .letterhead {
    position: absolute; left: 599px; top: 53px; width: 551px; height: 723px;
    border: 1.5px solid var(--sheet-border); background: var(--paper);
  }
  .letterhead .brand--corner { left: 451px; top: 96px; font-size: 26px; }
  .letterhead .brand--corner .brand-dot { width: 14px; height: 14px; }

  .watermark {
    position: absolute; left: 275px; top: 416px; transform: translate(-50%, -50%);
    width: 330px; height: 330px; border-radius: 50%; background: var(--faint);
    display: flex; align-items: center; justify-content: center;
    font-size: 48px; letter-spacing: 0.04em; color: var(--faint-text);
  }

  .letterhead-footer {
    position: absolute; left: 0; right: 0; top: 684px; text-align: center;
    font-size: 13.5px; line-height: 21px; color: var(--ink); white-space: nowrap;
  }
  .letterhead-footer .gap { margin-left: 6px; }
</style>
</head>
<body>
  <div class="canvas-frame"></div>

  <div class="brand brand--hero"><span class="brand-dot"></span>THE ORBIT</div>

  <section class="card card--front">
    <div class="brand"><span class="brand-dot"></span>THE ORBIT</div>
    <p class="card-holder">Your Name<br>Designation</p>
    <div class="card-divider"></div>
    <p class="card-contact">
      <span class="label">Address:</span><br>
      <span class="label">Ph.:</span>+91 9000 123 456<br>
      <span class="label">eMail:</span>connect@theorbit.com<br>
      <span class="label">Web:</span> www.theorbit.com
    </p>
  </section>

  <section class="card card--back">
    <div class="brand"><span class="brand-dot"></span>THE ORBIT</div>
  </section>

  <section class="letterhead">
    <div class="brand brand--corner"><span class="brand-dot"></span>THE ORBIT</div>
    <div class="watermark">THE ORBIT</div>
    <footer class="letterhead-footer">
      Address:<br>
      <span class="label">Ph.:</span> +91 9000 123 456
      <span class="label gap">eMail:</span> connect@theorbit.com
      <span class="label">Web:</span> www.theorbit.com
    </footer>
  </section>
</body>
</html>
```